Carpentry and Building Business Card

I'm looking for a business card that is minimalistic and that incorporates the theme of my Velmi logo.
On one side I'd like the VELMI logo with my details on the other side.
Double sided with curved edges

Target Market(s)

Construction / renovation
Adults

Industry/Entity Type

Tradesman

Contact Information for Business Card

Logo on one side, details on the other

Colors

Designer to choose only greyscale colors for use in the design.

Requirements
Must have
• Niko Barlettis
VELMI CONSTRUCT
Carpentry & Building Services
0412385726
Velmiconstruct@brindlemail.com
Lic No. 618243D
Nice to have
• Fb and insta icons. @velmiconstruct
Should not have
• No hammer or tool icons please.

No address line.

```html
<!DOCTYPE html>
<html lang="en">
<head>
<meta charset="UTF-8">
<title>Velmi Construct — Business Card</title>
<link href="https://fonts.googleapis.com/css2?family=Montserrat:wght@400;500;600;700&display=swap" rel="stylesheet">
<style>
  :root {
    --bg: #e2e2e2;
    --paper: #ffffff;
    --ink: #111111;
    --ink-soft: #333333;
    --night: #050505;
    --accent: #e8922c;
    --rule: #222222;
  }
  * { margin: 0; padding: 0; box-sizing: border-box; }
  html, body {
    width: 1200px; height: 1200px; overflow: hidden;
    background: var(--bg);
    font-family: "Montserrat", Arial, sans-serif;
  }
  .stage {
    width: 1200px; height: 1200px;
    display: flex; flex-direction: column; align-items: center; justify-content: center;
    gap: 48px;
  }
  .card {
    position: relative;
    width: 840px; height: 513px;
    border-radius: 22px;
    overflow: hidden;
    box-shadow: 0 10px 28px rgba(0,0,0,0.18);
  }
  .card--details { background: var(--paper); color: var(--ink); }
  .card--brand { background: var(--night); color: #fff; }

  .wordmark {
    position: absolute;
    display: flex; align-items: center; gap: 26px;
  }
  .wordmark__square {
    width: 64px; height: 64px;
    border: 3px solid var(--accent);
  }
  .wordmark__name {
    font-weight: 500;
    font-size: 62px;
    letter-spacing: 0.32em;
    line-height: 1;
  }
  .card--details .wordmark { top: 92px; left: 300px; }
  .card--details .wordmark__name { color: var(--ink); }
  .card--brand .wordmark { top: 50%; left: 50%; transform: translate(-50%, -50%); }
  .card--brand .wordmark__name { color: #fff; }

  .divider {
    position: absolute;
    left: 64px; right: 30px; top: 262px;
    height: 1.5px; background: var(--rule);
  }
  .person {
    position: absolute; left: 64px; top: 214px;
    font-size: 38px; font-weight: 500; line-height: 1;
  }
  .person__first { color: var(--accent); font-weight: 700; }
  .person__last { color: var(--ink); }

  .contacts {
    position: absolute; left: 64px; top: 282px;
    list-style: none;
    font-size: 22px; color: var(--ink-soft); line-height: 30px;
    letter-spacing: 0.02em;
  }
  .contacts li { display: flex; align-items: center; gap: 16px; }
  .contacts svg { width: 16px; height: 16px; flex: none; }
  .dot { width: 14px; height: 14px; border-radius: 50%; background: var(--accent); flex: none; margin: 0 1px; }

  .company {
    position: absolute; right: 56px; top: 282px;
    font-size: 22px; line-height: 30px; color: var(--ink-soft);
    letter-spacing: 0.02em;
  }
  .company__licence { color: var(--accent); }
</style>
</head>
<body>
<main class="stage">
  <section class="card card--details">
    <div class="wordmark">
      <span class="wordmark__square"></span>
      <span class="wordmark__name">VELMI.</span>
    </div>

    <h1 class="person"><span class="person__first">Niko</span> <span class="person__last">Barlettis</span></h1>
    <div class="divider"></div>

    <ul class="contacts">
      <li>
        <svg viewBox="0 0 16 16" aria-hidden="true"><path d="M4 1.5l2.2 3-1.4 1.6c.8 1.9 2.3 3.4 4.1 4.2l1.6-1.4 3 2.2-1.3 2.6C7 13.6 2.4 9 1.4 3z" fill="#e8922c"/></svg>
        0412385726
      </li>
      <li><span class="dot"></span>@velmiconstruct</li>
      <li><span class="dot"></span>/velmiconstruct</li>
      <li>
        <svg viewBox="0 0 16 16" aria-hidden="true"><rect x="1" y="3" width="14" height="10" rx="1.5" fill="#e8922c"/><path d="M1.5 4l6.5 5 6.5-5" stroke="#fff" stroke-width="1.4" fill="none"/></svg>
        Velmiconstruct@brindlemail.com
      </li>
      <li>
        <svg viewBox="0 0 16 16" aria-hidden="true"><circle cx="8" cy="8" r="6.5" fill="none" stroke="#e8922c" stroke-width="1.6"/><path d="M1.5 8h13M8 1.5c-3 3.5-3 9.5 0 13M8 1.5c3 3.5 3 9.5 0 13" stroke="#e8922c" stroke-width="1.2" fill="none"/></svg>
        www.Velmiconstruct.com
      </li>
    </ul>

    <div class="company">
      <p class="company__licence">Lic No. 618243D</p>
      <p>VELMI CONSTRUCT</p>
      <p>Carpentry &amp; Building Services</p>
    </div>
  </section>

  <section class="card card--brand">
    <div class="wordmark">
      <span class="wordmark__square"></span>
      <span class="wordmark__name">VELMI.</span>
    </div>
  </section>
</main>
</body>
</html>
```